A new updated business card. A good first impression for new customers to our business.

I need something unique. I will attached a picture of our old rubbish cards, and also our current Logo ( I think this needs an update if you have any ideas, its very basic and budget)The best way you will get to see my business is checking our Facebook page, I don't really know what else to say, but anything you want to know, ask away.www.facebook.com/tkwashworksco/

Target Market(s)

Home owners

Industry/Entity Type

Business

Contact Information for Business Card

T&K's Wash Works & Surface Guarding
Mira 0462 518 309 mira@tkwashworksco.com
Dunstan 0451 236 087 dunstan@tkwashworksco.com

FB: www.facebook.com/tkwashworksco/
Website: www.tkwashworksco.net (This is pretty rubbish- we don't really use it)

100% customer satisfaction guaranteed

All aspects of Hi-Pressure Cleaning
Sealing & Re-Sealing
Roof Cleaning
Colour sealing
Decorative coatings

Free no obligation quotes

Requirements
Must have
• NO OBLIGATION FREE quotes
• 100% Customer satisfaction guaranteed
• Can you please add both names, contact details and email address on one card.
• Dunstan 0451 236 087
• dunstan@tkwashworksco.com
• Mira 0462 518 309
• mira@tkwashworksco.com
• Please change the services:
• Hot/Cold Hi-Pressure Cleaning
• Sealing & Re-Sealing
• Roof Cleaning
• Colour Sealing
• Decorative Coatings
• Concrete Honing
• Thanks
Nice to have
• Something a bit different, something eye catching.l

```html
<!DOCTYPE html>
<html lang="en">
<head>
<meta charset="utf-8">
<title>T&amp;K's Wash Works – Business Card</title>
<link href="https://fonts.googleapis.com/css2?family=Roboto+Condensed:ital,wght@0,400;0,700;1,700&display=swap" rel="stylesheet">
<style>
  :root {
    --red: #e3121b;
    --black: #1a1a1a;
    --ink: #222222;
    --white: #ffffff;
    --stage-top: #d9d9d9;
    --stage-bottom: #9a9a9a;
    --divider: #999999;
  }
  * { box-sizing: border-box; margin: 0; padding: 0; }
  html, body { width: 1200px; height: 960px; overflow: hidden; }
  body {
    background: radial-gradient(ellipse at 50% 40%, var(--stage-top), var(--stage-bottom));
    font-family: "Roboto Condensed", "Arial Narrow", sans-serif;
    color: var(--ink);
    display: flex;
    flex-direction: column;
    align-items: center;
    justify-content: center;
    gap: 30px;
  }
  .card {
    position: relative;
    width: 760px;
    height: 434px;
    background: var(--white);
    box-shadow: 0 10px 30px rgba(0,0,0,.25);
    overflow: hidden;
  }
  .web-band {
    position: absolute;
    left: 0; right: 0; bottom: 44px;
    height: 62px;
    background: var(--red);
    color: var(--white);
    font-weight: 700;
    font-style: italic;
    font-size: 36px;
    display: flex;
    align-items: center;
    padding-left: 48px;
    letter-spacing: .5px;
  }
  .brand-name {
    color: var(--red);
    font-weight: 700;
    line-height: 1.05;
  }

  /* Services side */
  .services .hero-art {
    position: absolute;
    left: 230px; top: 18px;
    width: 330px; height: 150px;
    border-radius: 50%;
    background: radial-gradient(ellipse at 50% 60%, #ffffff 55%, #e6e6e6 70%, #bcbcbc 100%);
  }
  .services .hero-brand {
    position: absolute;
    left: 295px; top: 60px;
    width: 200px;
    text-align: center;
    font-size: 22px;
  }
  .services .tagline {
    position: absolute;
    left: 0; right: 0; top: 180px;
    text-align: center;
  }
  .services .sector { font-size: 26px; }
  .services .quality { font-size: 48px; font-weight: 700; color: var(--black); letter-spacing: 1px; line-height: 1.05; }
  .services .service-list {
    position: absolute;
    left: 20px; right: 20px; top: 262px;
    text-align: center;
    font-size: 21px;
    line-height: 1.3;
  }
  .service-list .dot { color: var(--red); padding: 0 4px; }

  /* Contact side */
  .contact .brand-block {
    position: absolute;
    left: 40px; top: 30px;
    font-size: 30px;
    width: 260px;
  }
  .guarantee-seal {
    position: absolute;
    left: 58px; top: 124px;
    width: 144px; height: 144px;
    border-radius: 50%;
    background: var(--red);
    display: flex;
    align-items: center;
    justify-content: center;
  }
  .guarantee-seal .seal-inner {
    width: 124px; height: 124px;
    border-radius: 50%;
    border: 2px solid var(--white);
    color: var(--white);
    display: flex;
    flex-direction: column;
    align-items: center;
    justify-content: center;
    text-align: center;
    font-weight: 700;
    text-transform: uppercase;
    line-height: 1.05;
  }
  .seal-inner .seal-top,
  .seal-inner .seal-bottom { font-size: 11px; letter-spacing: .5px; }
  .seal-inner .seal-percent { font-size: 40px; font-style: italic; margin: 2px 0; }
  .contact .quote-flag {
    position: absolute;
    right: 0; top: 0;
    width: 170px; height: 120px;
    background: var(--black);
    color: var(--white);
    font-weight: 700;
    font-size: 26px;
    display: flex;
    align-items: center;
    justify-content: center;
    text-align: center;
    line-height: 1.1;
  }
  .quote-flag .get { color: var(--red); display: block; font-size: 30px; }
  .quote-flag .no-obligation { display: block; font-size: 14px; font-weight: 400; letter-spacing: 1px; text-transform: uppercase; margin-top: 4px; }
  .contact .people {
    position: absolute;
    left: 300px; top: 128px;
    width: 420px;
  }
  .person {
    display: grid;
    grid-template-columns: 1fr auto 28px;
    grid-template-rows: auto auto;
    column-gap: 10px;
    align-items: center;
    margin-bottom: 14px;
  }
  .person .name { grid-column: 1; color: var(--red); font-weight: 700; font-style: italic; font-size: 24px; border-right: 1px solid var(--divider); padding-right: 8px; }
  .person .phone { grid-column: 2; font-weight: 700; font-size: 30px; color: var(--black); }
  .person .email { grid-column: 1 / 3; font-size: 18px; }
  .icon { width: 24px; height: 24px; display: block; }
  .fb-line {
    display: flex; align-items: center; justify-content: space-between;
    font-size: 18px; font-weight: 700;
    padding-right: 2px;
  }
</style>
</head>
<body>

<section class="card services">
  <div class="hero-art" role="img" aria-label="Illustration of a pressure washer wand with a curved hose and blue spray"></div>
  <div class="hero-brand brand-name">T&amp;K's Wash Works &amp; Surface Guarding</div>
  <div class="tagline">
    <p class="sector">Residential &amp; Commercial</p>
    <p class="quality">QUALITY EVERYTIME</p>
  </div>
  <p class="service-list">
    Hot/Cold Hi-Pressure Cleaning<span class="dot">•</span>Sealing &amp; Re-Sealing<span class="dot">•</span>Concrete Honing<br>
    Roof Cleaning<span class="dot">•</span>Colour Sealing<span class="dot">•</span>Decorative Coatings
  </p>
  <div class="web-band">www.tkwashworksco.net</div>
</section>

<section class="card contact">
  <div class="brand-block brand-name">T&amp;K's Wash Works &amp; Surface Guarding</div>
  <div class="guarantee-seal">
    <div class="seal-inner">
      <span class="seal-top">Customer<br>Satisfaction</span>
      <span class="seal-percent">100%</span>
      <span class="seal-bottom">Guaranteed</span>
    </div>
  </div>
  <div class="quote-flag"><p><span class="get">Get</span>Free Quotes<span class="no-obligation">No Obligation</span></p></div>

  <div class="people">
    <div class="person">
      <span class="name">Dunstan</span>
      <span class="phone">0451 236 087</span>
      <svg class="icon" viewBox="0 0 24 24"><circle cx="12" cy="12" r="12" fill="var(--red)"/><rect x="8.5" y="5" width="7" height="14" rx="1.5" fill="none" stroke="#fff" stroke-width="1.6"/><circle cx="12" cy="16.5" r="1" fill="#fff"/></svg>
      <span class="email">dunstan@tkwashworksco.com</span>
      <svg class="icon" viewBox="0 0 24 24"><rect x="2" y="5" width="20" height="14" rx="1" fill="var(--red)"/><path d="M2 6 L12 13 L22 6" fill="none" stroke="#fff" stroke-width="1.6"/></svg>
    </div>
    <div class="person">
      <span class="name">Mira</span>
      <span class="phone">0462 518 309</span>
      <svg class="icon" viewBox="0 0 24 24"><circle cx="12" cy="12" r="12" fill="var(--red)"/><rect x="8.5" y="5" width="7" height="14" rx="1.5" fill="none" stroke="#fff" stroke-width="1.6"/><circle cx="12" cy="16.5" r="1" fill="#fff"/></svg>
      <span class="email">mira@tkwashworksco.com</span>
      <svg class="icon" viewBox="0 0 24 24"><rect x="2" y="5" width="20" height="14" rx="1" fill="var(--red)"/><path d="M2 6 L12 13 L22 6" fill="none" stroke="#fff" stroke-width="1.6"/></svg>
    </div>
    <p class="fb-line"><span>fb.com/tkwashworksco</span>
      <svg class="icon" viewBox="0 0 24 24"><circle cx="12" cy="12" r="12" fill="var(--red)"/></svg>
    </p>
  </div>
  <div class="web-band">www.tkwashworksco.net</div>
</section>

</body>
</html>
```